May/June Newsletter

We require a newsletter with as much infographic as possible

Attached is our previous newsletter as an example.

ONLY USE THE DATA IN EPC CHALLENGES

Target Market(s)

property market

Requirements
Must have
• Company colours and logo from
www.verdanthaus.co.uk

be similar to our previous newsletter. copy attached.

must have a screenshot of VHConnect attached

```html
<!DOCTYPE html>
<html lang="en">
<head>
<meta charset="utf-8">
<title>Verdant Haus – May/June Newsletter</title>
<link href="https://fonts.googleapis.com/css2?family=Raleway:wght@300;400;600;700&display=swap" rel="stylesheet">
<style>
:root{
  --page:#efeeee;
  --card:#ffffff;
  --teal:#16a393;
  --teal-dark:#0f7f74;
  --teal-light:#2cc3b0;
  --ink:#4d4d4d;
  --ink-dark:#2b2b2b;
  --rule:#d9d9d9;
  --link:#d0202f;
  --brand-green:#3aa23a;
  --band-a:#2f6b0f;--band-b:#7cb51e;--band-c:#c4da1c;--band-d:#ecc416;
  --band-e:#f0a00c;--band-f:#e0620c;--band-g:#e01010;
  --screen:#2aa7e0;
}
*{margin:0;padding:0;box-sizing:border-box}
html,body{width:1200px;height:4229px;overflow:hidden;background:var(--page)}
body{font-family:"Raleway",Arial,sans-serif;color:var(--ink);position:relative}
.abs{position:absolute}
.preheader{left:0;width:1200px;top:68px;text-align:center;font-family:Arial,sans-serif;font-size:19px;line-height:26px;color:#444}
.preheader a{color:var(--link)}
.card{left:233px;top:149px;width:738px;height:3795px;background:var(--card);border-radius:16px}
.brand{font-weight:700;font-size:34px;color:var(--ink-dark);letter-spacing:-.5px;display:flex;align-items:center;gap:10px}
.brand .dot{width:26px;height:26px;border-radius:50%;background:var(--brand-green)}
.header-mail{right:251px;top:219px;font-size:18px;color:#555;display:flex;align-items:center;gap:12px}
.icon-circle{width:34px;height:34px;border:2px solid #999;border-radius:50%;display:flex;align-items:center;justify-content:center}
.hero{left:260px;top:283px;width:680px;height:367px;background:linear-gradient(135deg,var(--teal-dark),var(--teal) 55%,#1bb0a0)}
.hero h1{position:absolute;left:34px;top:60px;color:#fff;font-weight:700;font-size:38px;line-height:45px;letter-spacing:.5px}
.hero .btn{position:absolute;left:34px;top:267px;width:184px;height:52px;background:var(--teal-light);color:#fff;font-weight:700;font-size:16px;display:flex;align-items:center;justify-content:center;letter-spacing:.5px}
.hero .art{position:absolute;left:327px;top:63px;width:336px;height:294px;background:radial-gradient(ellipse at 50% 80%,#6aa52c 0,#4d8a2a 30%,rgba(255,255,255,0) 60%);border-radius:8px}
.section-title{left:260px;top:670px;font-size:31px;font-weight:600;color:var(--teal)}
.date{left:260px;font-size:24px;font-weight:600;color:var(--teal);display:flex;align-items:center;gap:12px}
.sub{left:260px;font-size:22px;font-weight:600;color:var(--teal)}
.copy{left:260px;width:662px;font-size:18px;line-height:29.5px;font-weight:400}
.rule{left:260px;width:680px;height:2px;background:var(--rule)}
.epc{left:260px;top:2098px}
.band{position:absolute;left:0;height:42px;color:#fff;font-size:27px;font-weight:400;padding-left:8px;line-height:42px}
.readmore{left:260px;top:2705px;font-size:17px;font-weight:700;color:var(--teal)}
.rating-label{font-family:Arial,sans-serif;font-size:13px;color:#444;text-align:center;line-height:17px}
.rating-label b{color:var(--screen);font-weight:400}
.monitor{background:linear-gradient(180deg,var(--screen) 0,var(--screen) 62%,#d2d2d2 62%,#c4c4c4 100%);border-radius:2px}
.footer-contact h4{font-size:19px;font-weight:700;color:var(--teal);margin-bottom:18px}
.footer-contact li{list-style:none;display:flex;gap:12px;font-size:18px;line-height:27px;color:#555;margin-bottom:14px}
.footer-contact svg{flex:0 0 20px;margin-top:4px}
.social{width:42px;height:42px;border:2px solid #333;border-radius:50%}
.copyright{left:233px;width:738px;top:3873px;text-align:center;font-size:18px;color:#444}
</style>
</head>
<body>
<div class="abs preheader">Is this email not displaying correctly?<br><a href="#">View it in your browser.</a></div>

<div class="abs card"></div>

<div class="abs brand" style="left:260px;top:205px">VERDANT HAUS<span class="dot"></span></div>
<div class="abs header-mail"><span class="icon-circle"><svg width="16" height="12" viewBox="0 0 16 12"><rect x="1" y="1" width="14" height="10" fill="none" stroke="#999" stroke-width="1.5"/><path d="M1 1l7 6 7-6" fill="none" stroke="#999" stroke-width="1.5"/></svg></span>info@verdanthaus.co.uk</div>

<div class="abs hero">
  <h1>ENERGY<br>PERFORMANCE<br>IMPROVEMENT<br>SERVICES</h1>
  <div class="btn">GET IN TOUCH</div>
  <div class="art" role="img" aria-label="Illustration of two wind turbines on a grassy island"></div>
</div>

<div class="abs section-title">EPC CHALLENGES</div>
<div class="abs date" style="top:714px"><svg width="24" height="24" viewBox="0 0 24 24"><rect x="2" y="4" width="20" height="18" fill="none" stroke="currentColor" stroke-width="2"/><path d="M2 9h20M7 1v5M17 1v5M6 13h3M11 13h3M16 13h3M6 17h3M11 17h3" stroke="currentColor" stroke-width="2"/></svg>April 2023</div>
<p class="abs copy" style="top:758px">From April 2023 existing MEES regulations will be extended to cover all non-domestic tenancies (already in place for domestic tenancies since 1st April 2020).</p>
<p class="abs copy" style="top:875px">MEES (Minimum Energy Efficiency Standard) regulations make it unlawful to agree a new lease on a property with an EPC rating below an E unless an exemption has been put in place on the PRS register.</p>
<div class="abs rule" style="top:979px"></div>

<div class="abs date" style="top:1028px"><svg width="24" height="24" viewBox="0 0 24 24"><rect x="2" y="4" width="20" height="18" fill="none" stroke="currentColor" stroke-width="2"/><path d="M2 9h20M7 1v5M17 1v5M6 13h3M11 13h3M16 13h3M6 17h3M11 17h3" stroke="currentColor" stroke-width="2"/></svg>Beyond April 2023</div>
<div class="abs" style="left:260px;top:1097px;width:680px;height:378px;background:radial-gradient(circle at 55% 35%,#c7e38f 0,#aed66c 45%,#9acb58 100%)" role="img" aria-label="Illustration of a lightbulb with plants, solar panels, wind turbines and a plug"></div>
<p class="abs copy" style="top:1518px">The UK Governments long term aim of having net zero carbon emissions by 2050 has several key dates before to make this achievable.</p>
<p class="abs copy" style="top:1606px">Consultation process closed in January this year into the minimum energy standards for non domestic properties.&nbsp; The consultation process looked into the future trajectory of measures up to 2030, with one suggestion being for commercial properties to be of minimum band C or B.</p>
<p class="abs copy" style="top:1755px">The Clean Growth Strategy is already in place to help as many domestic properties achieve band C by 2035.<br>The definition is two-pronged. Firstly, during the construction process of an asset, the amount of carbon emissions produced should be zero, or negative through the use of offsets or the export of on-site renewable energy. Secondly, during the use of the building, the amount of carbon emissions produced from the building's operational energy should also be zero or negative.</p>
<div class="abs rule" style="top:2010px"></div>

<div class="abs sub" style="top:2032px">Ongoing</div>
<div class="abs epc">
  <svg width="320" height="356" viewBox="0 0 320 356" style="position:absolute;left:0;top:0">
    <polygon points="0,0 75,0 101,21 75,42 0,42" fill="var(--band-a)"/>
    <polygon points="0,52 117,52 143,73 117,94 0,94" fill="var(--band-b)"/>
    <polygon points="0,105 150,105 176,126 150,147 0,147" fill="var(--band-c)"/>
    <polygon points="0,157 184,157 210,178 184,199 0,199" fill="var(--band-d)"/>
    <polygon points="0,210 217,210 243,231 217,252 0,252" fill="var(--band-e)"/>
    <polygon points="0,262 251,262 277,283 251,304 0,304" fill="var(--band-f)"/>
    <polygon points="0,314 284,314 310,335 284,356 0,356" fill="var(--band-g)"/>
  </svg>
  <div class="band" style="top:0">A</div>
  <div class="band" style="top:52px">B</div>
  <div class="band" style="top:105px">C</div>
  <div class="band" style="top:157px">D</div>
  <div class="band" style="top:210px">E</div>
  <div class="band" style="top:262px">F</div>
  <div class="band" style="top:314px">G</div>
</div>
<div class="abs" style="left:619px;top:2098px;width:304px;height:332px;background:linear-gradient(180deg,#7fae1e 0,#5f8f17 38%,#f3ead2 40%,#ece0c0 100%)" role="img" aria-label="Illustration of a house with a green roof"></div>

<p class="abs copy" style="top:2487px">From April 2023 existing MEES regulations will be extended to cover all non-domestic tenancies (already in place for domestic tenancies since 1st April 2020).</p>
<p class="abs copy" style="top:2606px">MEES (Minimum Energy Efficiency Standard) regulations make it unlawful to agree a new lease on a property with an EPC rating below an E unless an exemption has been put in place on the PRS register.</p>
<div class="abs readmore">Read More &gt;</div>
<div class="abs rule" style="top:2773px"></div>

<p class="abs copy" style="top:2804px">Verdant Haus have developed a market leading EPC management tool to meet the current and ongoing EPC challenges faced in the property market.</p>
<div class="abs" style="left:336px;top:2885px;width:482px;height:283px;background:radial-gradient(ellipse at 50% 55%,#c9c9c9 0,#b3b3b3 40%,#f4f4f4 75%,#fff 100%)" role="img" aria-label="Illustration of a grey commercial warehouse building"></div>

<div class="abs rating-label" style="left:330px;top:3203px;width:180px">Previous rating<br><b>EnCalc 3.4a</b> = Band D 89</div>
<div class="abs rating-label" style="left:628px;top:3203px;width:200px">Current rating<br><b>EnCalc 5.6a</b> = Band E 101</div>
<div class="abs monitor" style="left:355px;top:3255px;width:130px;height:142px" role="img" aria-label="Illustration of a computer showing the previous band D rating"></div>
<svg class="abs" style="left:495px;top:3283px" width="150" height="34" viewBox="0 0 150 34">
  <polygon points="0,17 20,0 20,8 130,8 130,0 150,17 130,34 130,26 20,26 20,34" fill="var(--screen)"/>
  <text x="75" y="22" font-family="Arial,sans-serif" font-weight="700" font-size="13" fill="#fff" text-anchor="middle">10 years span</text>
</svg>
<div class="abs monitor" style="left:647px;top:3255px;width:160px;height:142px" role="img" aria-label="Illustration of a computer showing the current band E rating"></div>

<p class="abs copy" style="top:3458px">We are currently offering free trials on VHConnect to demonstrate how we can assist to manage the above challenges.</p>
<div class="abs rule" style="top:3600px"></div>

<div class="abs brand" style="left:260px;top:3654px;font-size:30px">VERDANT HAUS<span class="dot" style="width:22px;height:22px"></span></div>
<div class="abs social" style="left:260px;top:3718px" aria-label="Social profile link"></div>
<div class="abs social" style="left:313px;top:3718px" aria-label="Social profile link"></div>

<div class="abs footer-contact" style="left:655px;top:3668px;width:300px">
  <h4>CONTACT DETAILS</h4>
  <ul>
    <li><svg width="20" height="18" viewBox="0 0 20 18"><path d="M10 1L1 9h3v8h5v-5h2v5h5V9h3z" fill="#666"/></svg>Verdant Haus Limited</li>
    <li><svg width="20" height="20" viewBox="0 0 20 20"><path d="M10 1a6 6 0 00-6 6c0 5 6 12 6 12s6-7 6-12a6 6 0 00-6-6z" fill="none" stroke="#666" stroke-width="1.6"/><circle cx="10" cy="7" r="2" fill="#666"/></svg>Fenwick Court, 18-22 Alder Road,London, N1 5QT</li>
    <li><svg width="20" height="16" viewBox="0 0 20 16"><rect x="1" y="1" width="18" height="13" fill="none" stroke="#666" stroke-width="1.5"/><path d="M1 1l9 7 9-7" fill="none" stroke="#666" stroke-width="1.5"/></svg>info@ verdanthaus.co.uk</li>
  </ul>
</div>

<div class="abs copyright">Copyright Verdant Haus Limited - All rights reserved ©2016.</div>
<div class="abs rule" style="left:262px;width:676px;top:3967px;height:1px;background:#cfcfcf"></div>
</body>
</html>
```